Veltrane Business Card - Construction Management

Create a business card for a construction management firm that owns/responsible for three other companies and include the following:
Main Company & Logo - Veltrane Management Group Ltd.
Subsidiary Company Logo only to appear on card in miniature form :
Quelbrin Industrial Services Ltd.
Halvoran Sisters Construction Inc.
Tessaly Groundworks

Contact Information for Business Card

Veltrane Management Group Ltd.
872 Brelford Road - Coville Industrial Park
RM of Danbrook
Regina, Saskatchewan
S7T 2B9
P: 306.555.0182
C: 306.555.0147
e:jtorvelli@veltrane-example.ca

Colors

Designer to choose colors to be used in the design.

Requirements
Must have
• Main Logo and small/miniature version of three subsidiary company logos.
• We would appreciate seeing a version of main logo(Veltrane Group) on front of card and other three miniature/small logos on the front of the card or version of main logo on front and other three logos on the back of the card.

```html
<!DOCTYPE html>
<html lang="en">
<head>
<meta charset="utf-8">
<title>Veltrane Business Card</title>
<link rel="stylesheet" href="https://fonts.googleapis.com/css2?family=Roboto:wght@400;500;700&family=Roboto+Condensed:wght@700&display=swap">
<style>
  :root {
    --backdrop: #3a3a3a;
    --card-white: #f3f3f3;
    --brand-blue: #1277be;
    --brand-grey: #7a7a7a;
    --text-grey: #555555;
    --white: #ffffff;
  }
  * { margin: 0; padding: 0; box-sizing: border-box; }
  html, body {
    width: 1200px; height: 960px; overflow: hidden;
    background: var(--backdrop);
    font-family: "Roboto", Arial, sans-serif;
  }
  .card {
    position: absolute;
    width: 600px; height: 343px;
  }
  .card-front { left: 314px; top: 113px; background: var(--card-white); }
  .card-back  { left: 311px; top: 472px; background: var(--brand-blue); }

  .name-band {
    position: absolute; left: 0; top: 39px;
    width: 318px; height: 91px;
    background: var(--brand-blue);
    color: var(--white);
    padding: 18px 0 0 33px;
  }
  .holder-name { font-size: 24px; font-weight: 700; letter-spacing: 0.3px; line-height: 1.2; }
  .holder-title { font-size: 17px; font-weight: 400; margin-top: 1px; }

  .brand-lockup {
    position: absolute; left: 300px; top: 48px;
    display: flex; align-items: center; gap: 12px;
  }
  .brand-mark {
    width: 64px; height: 64px; background: var(--brand-blue);
  }
  .brand-name {
    font-family: "Roboto", Arial, sans-serif;
    font-weight: 700; font-size: 27px; line-height: 1.05;
    color: var(--brand-blue);
    letter-spacing: 0.5px;
  }

  .contact-list {
    position: absolute; left: 33px; top: 241px;
    font-size: 14.5px; line-height: 19px; color: var(--text-grey);
    list-style: none;
  }
  .contact-web { letter-spacing: 1.6px; }

  .address {
    position: absolute; right: 33px; top: 243px;
    text-align: right; font-style: normal;
    font-size: 14.5px; line-height: 19px; color: var(--text-grey);
  }
  .address-company {
    font-family: "Roboto Condensed", Arial, sans-serif;
    font-weight: 700;
  }

  .back-brand {
    position: absolute; left: 0; right: 0; top: 92px;
    display: flex; flex-direction: column; align-items: center; gap: 16px;
    color: var(--white);
  }
  .back-brand-mark { width: 70px; height: 70px; background: var(--white); }
  .back-brand-name { font-size: 30px; font-weight: 700; letter-spacing: 1px; }

  .subsidiaries {
    position: absolute; left: 0; right: 0; top: 276px;
    display: flex; justify-content: center; gap: 26px;
    list-style: none;
  }
  .subsidiary {
    display: flex; align-items: center; gap: 6px;
    color: var(--white); font-size: 11px; font-weight: 700;
  }
  .subsidiary-dot { width: 10px; height: 10px; border-radius: 50%; background: var(--white); }
</style>
</head>
<body>
  <section class="card card-front" aria-label="Card front">
    <div class="name-band">
      <div class="holder-name">AREN CASTELL</div>
      <div class="holder-title">CEO/FOUNDER</div>
    </div>
    <div class="brand-lockup">
      <div class="brand-mark"></div>
      <div class="brand-name">VELTRANE<br>GROUP</div>
    </div>
    <ul class="contact-list">
      <li>Phone: 306.555.0182</li>
      <li>Mob: 306.555.0147</li>
      <li>jtorvelli@veltrane-example.ca</li>
      <li class="contact-web">www.veltrane-example.ca</li>
    </ul>
    <address class="address">
      <div class="address-company">Veltrane Management Group Ltd</div>
      <div>872 Brelford Road - Coville</div>
      <div>Industrial Park, RM of Danbrook</div>
      <div>Regina, Saskatchewan, S7T 2B9</div>
    </address>
  </section>

  <section class="card card-back" aria-label="Card back">
    <div class="back-brand">
      <div class="back-brand-mark"></div>
      <div class="back-brand-name">VELTRANE GROUP</div>
    </div>
    <ul class="subsidiaries">
      <li class="subsidiary"><span class="subsidiary-dot"></span>Halvoran Sisters Construction Inc.</li>
      <li class="subsidiary"><span class="subsidiary-dot"></span>Quelbrin Industrial Services Ltd.</li>
      <li class="subsidiary"><span class="subsidiary-dot"></span>Tessaly Groundworks</li>
    </ul>
  </section>
</body>
</html>
```